Web Design Project

8 page static website.
About us/What we stand for:
Forno Lucente CBD plans to make a huge splash in Sydney by being the first Italian pizza and pasta retail food outlet offering truly fresh, nutritious ingredients – herbs and vegetables are picked directly from the garden, pizzas are made with love in a fun filled atmosphere and a cutting edge brand strategy that promotes a happy lifestyle and reminds people that happiness and togetherness comes from sharing amazing food.
The best thing about Forno Lucente is that it offers consumers a choice to either choose from the enticing gluten free and vegetarian menu range to the more traditional pizza and pasta, we cater for their own tastes, this provides a distinct point of difference in the retail food market, as well as allowing consumers to have an endless range of choices without having to worry about the nutritional value.
Consumers have now become accustomed to a consistent brand experience which is setting increasingly high standards when it comes to food quality, taste and service.
We want to capitalise on the opportunity to create a strong, modern brand that promotes healthy lifestyle habits, sells fresh, wholesome ingredients, delivers
exceptional service in a fun filled atmosphere and appeals to a broad market.
Our business model is specifically pickup and delivery with a few seats and crates for eating in. It is for the time poor that still want to have a great tasting Italian experience with pizza and pasta within the quick service restaurant space. Takeaway, office catering and delivery will be a large percentage of our business.
Our philosophy at Forno Lucente is simple:
“Success is not a formula, it’s a recipe”.
Brand personality:
We are located in a laneway and basically the shop is a hole in the one. It looks like a restaurant you would see in Italy.
Modern Italian, contemporary, fun, rustic (Taco Vela, Brasa’s)
1 Aims of this website
• Emotionally connect with the target audience to reflect (“happiness and togetherness comes from sharing amazing food”)
• To entice people to order pizza
• To capture a mailing list
• To differentiate us from the low cost, low quality pizza
• To create a connection with the target audience, and promote word of mouth
2 Target audience(s)
• Male/Female
• 18-49
• Sydney CBD and Woolloomooloo
• Internet Savvy.
3. Contents/Functionality
www.crustwagon.com.au – like the rustic brown in the website and the old washed out white colour through the font.
Target Market(s)
18-49 years old
City worker and resident
people that enjoy good food
Industry/Entity Type
Restaurant
Requirements
Must have
- Some splash of red and green to represent the italian theme.
Attached is a draft of the homepage layout.
Attached below are some fonts that we like.
Nice to have
- Please see http://www.brasashop.com.au/Pages/locationmenu.aspx
This is how our takeaway menu looks like.

```html
<!DOCTYPE html>
<html lang="en">
<head>
<meta charset="utf-8">
<title>Forno Lucente – Caffè Pizzeria</title>
<link rel="stylesheet" href="https://fonts.googleapis.com/css2?family=Oswald:wght@500&family=Gelasio:ital,wght@0,400;1,400&family=Arimo:wght@700&display=swap">
<style>
:root{
  --paper:#f3e2c0;
  --paper-edge:#e6cfa2;
  --panel:#f6e8ca;
  --panel-line:#ead5ac;
  --tape:#e8d49a;
  --red:#cc3a28;
  --green:#7d9a1f;
  --tan:#d39d58;
  --brown:#8a6d4c;
  --dark:#3e3528;
  --field:#ecd5a0;
}
*{box-sizing:border-box;margin:0;padding:0}
html,body{width:1200px;height:954px;overflow:hidden}
body{
  position:relative;
  background:radial-gradient(ellipse at 50% 40%,#f7ead0 0%,var(--paper) 55%,var(--paper-edge) 100%);
  font-family:"Gelasio",Georgia,serif;
  color:var(--brown);
}
.brand{position:absolute;left:220px;top:70px;display:flex;align-items:center;gap:10px}
.brand-dot{width:22px;height:22px;border-radius:50%;background:var(--red)}
.brand-name{font-family:"Gelasio",Georgia,serif;font-size:26px;color:var(--red)}
.follow{position:absolute;right:217px;top:36px;display:flex;align-items:center;gap:7px;font-size:17px;color:#7d6a52}
.follow span{margin-right:8px}
.social{width:24px;height:24px;border-radius:50%}
.social.s1{background:#e9882c}.social.s2{background:#2f5f9f}.social.s3{background:#5cb6e6}
.order-now{position:absolute;right:217px;top:66px;font-size:17px;color:#7d6a52}
.order-now b{font-weight:400;font-size:24px;color:var(--red);margin-left:6px}
.nav{position:absolute;left:0;top:114px;width:1200px;height:43px}
.nav a{position:absolute;top:0;height:43px;line-height:43px;font-family:"Oswald",sans-serif;font-size:20px;color:var(--red);text-decoration:none;text-align:center}
.nav a.active{background:var(--tape);color:var(--green);box-shadow:0 1px 3px rgba(120,90,40,.25)}
.hero{position:absolute;left:215px;top:169px;width:770px;height:355px;background:var(--panel);border:1px solid var(--panel-line)}
.hero-copy{position:absolute;left:40px;top:85px;font-family:"Arimo",Arial,sans-serif}
.hero-title{font-size:32px;line-height:30px;color:var(--tan)}
.hero-title small{display:block;font-size:31px;font-weight:400;opacity:.95}
.hero-price{font-size:50px;line-height:56px;color:var(--red);margin-top:4px}
.hero-tag{font-size:22px;color:var(--green);margin-top:8px}
.hero-note{font-size:11px;color:var(--dark);margin-top:4px}
.hero-call{margin-top:18px;font-size:15px;color:var(--red)}
.hero-call b{font-size:32px;margin-left:8px}
.pizza{position:absolute;left:578px;top:194px;width:396px;height:396px;border-radius:50%;
  background:radial-gradient(circle at 50% 50%,#d8472b 0%,#c43a22 55%,#d89a4e 88%,#e8b673 100%);
  box-shadow:0 6px 14px rgba(90,50,20,.35)}
.cards{position:absolute;top:534px;left:215px}
.card{position:absolute;top:0;width:247px;height:203px;background:var(--panel);border:1px solid var(--panel-line)}
.card h2{position:absolute;left:17px;top:14px;font-family:"Oswald",sans-serif;font-weight:500;font-size:20px;letter-spacing:.2px}
.club{left:0}.club h2{color:var(--green)}
.field{position:absolute;left:18px;width:212px;height:31px;background:var(--field);font-size:15px;color:#9a7a4e;padding:5px 6px}
.join{position:absolute;right:20px;top:150px;width:78px;height:30px;background:var(--tape);font-family:"Oswald",sans-serif;font-size:14px;color:var(--tan);text-align:center;line-height:30px;box-shadow:0 1px 3px rgba(120,90,40,.25)}
.catering{left:262px}.catering h2,.area h2{color:var(--red)}
.area{left:523px}
.photo{position:absolute;left:21px;top:55px;width:204px;height:100px;background:linear-gradient(135deg,#4a3b30,#a88a5d 55%,#efe3cc)}
.map{position:absolute;left:18px;top:55px;width:196px;height:92px;background:linear-gradient(180deg,#e9b68a,#e2a676);border-radius:30px 40px 20px 50px;opacity:.8}
.card-link{position:absolute;left:20px;top:171px;font-family:"Oswald",sans-serif;font-size:12px;color:var(--tan)}
.quote{position:absolute;left:215px;top:750px;width:770px;height:84px;background:var(--panel);border:1px solid var(--panel-line)}
.quote p{position:absolute;left:30px;top:18px;width:730px;font-style:italic;font-size:13.5px;line-height:17px;color:#9a7f5e}
.quote p::before{content:"\201C";position:absolute;left:-10px;top:-4px;font-size:18px;color:#b9a27f}
.quote cite{position:absolute;right:25px;top:56px;font-style:normal;font-size:13.5px;color:var(--green)}
.footer-nav{position:absolute;top:847px;left:0;width:1200px;text-align:center;font-size:14px;color:#9a7f5e}
.footer-nav a{color:#9a7f5e;text-decoration:none;margin:0 8px}
.copyright{position:absolute;top:870px;left:0;width:1200px;text-align:center;font-size:13.5px;color:#9a7f5e}
.order-tab{position:absolute;left:1058px;top:393px;width:142px;height:82px;background:#f4e5c3;box-shadow:0 1px 4px rgba(100,70,30,.3)}
.order-tab .o1{position:absolute;left:12px;top:8px;font-family:"Oswald",sans-serif;font-size:13px;color:var(--green)}
.order-tab .o2{position:absolute;left:12px;top:24px;font-family:"Oswald",sans-serif;font-size:19px;letter-spacing:3px;color:var(--red)}
.order-tab .o3{position:absolute;left:10px;top:53px;background:#f9edd6;padding:2px 4px;font-family:"Oswald",sans-serif;font-size:10px;color:var(--red)}
.courier{position:absolute;left:1142px;top:369px;width:58px;height:106px;background:linear-gradient(180deg,#d43626,#c22a1e 60%,#e39a57)}
</style>
</head>
<body>
<header>
  <div class="brand"><span class="brand-dot"></span><span class="brand-name">Forno Lucente</span></div>
  <div class="follow"><span>Follow us</span><i class="social s1"></i><i class="social s2"></i><i class="social s3"></i></div>
  <div class="order-now">Order Now<b>9000 5120 4477</b></div>
  <nav class="nav">
    <a href="#" style="left:561px;width:48px">HOME</a>
    <a href="#" class="active" style="left:648px;width:106px">ABOUT US</a>
    <a href="#" style="left:794px;width:45px">MENU</a>
    <a href="#" style="left:890px;width:93px">CONTAC US</a>
  </nav>
</header>

<section class="hero">
  <div class="hero-copy">
    <div class="hero-title">Buy Family Pan<small>for only</small></div>
    <div class="hero-price">$39.00</div>
    <div class="hero-tag">ALL YOU PAY!</div>
    <div class="hero-note">Exclusive for delivery. Valid from December 4- 10.2011</div>
    <div class="hero-call">Call<b>9000-5120-4477</b></div>
  </div>
</section>
<div class="pizza" role="img" aria-label="Mushroom and herb pizza with one slice pulled out"></div>

<section class="cards">
  <div class="card club">
    <h2>JOIN OUR EMAIL CLUB</h2>
    <div class="field" style="top:66px">Name:</div>
    <div class="field" style="top:114px">Email:</div>
    <div class="join">JOIN NOW</div>
  </div>
  <div class="card catering">
    <h2>OFFICE CATERING</h2>
    <div class="photo" role="img" aria-label="Photo of a catered office buffet table"></div>
    <div class="card-link">READ MORE</div>
  </div>
  <div class="card area">
    <h2>DELIVERY AREA</h2>
    <div class="map" role="img" aria-label="Dotted world map showing delivery locations"></div>
    <div class="card-link">CLICK HERE TO FIND YOUR LOCATION</div>
  </div>
</section>

<section class="quote">
  <p>Lorem Ipsum is simply dummy text of the printing and typesetting industry. Lorem Ipsum has been the industry's standard dummy text ever since the 1500s...</p>
  <cite>Mr. Bruno</cite>
</section>

<footer>
  <div class="footer-nav"><a href="#">Home</a>|<a href="#">About Us</a>|<a href="#">Menu</a>|<a href="#">Contact Us</a>|<a href="#">Newsletter</a>|<a href="#">Delivery Area</a>|<a href="#">Privacy Policy</a></div>
  <div class="copyright">Copyright 2011 your company. All rights reserved.</div>
</footer>

<aside class="order-tab">
  <span class="o1">ORDER</span>
  <span class="o2">ONLINE</span>
  <span class="o3">CLICK HERE !</span>
</aside>
<div class="courier" role="img" aria-label="Delivery courier in red cap holding a pizza"></div>
</body>
</html>
```